MODELS AGENCY NEW YEAR 2026 CARD

A 10 cm x 21 cm horizontal New Year card for clients of our 2 models agencies, Pommelin (kids) and Velvaride (actors and adults) (logo in the jobs).

Side A of the card: creative mission:
-text: 2026
-text: Peace and Love
-Studio or movie set atmosphere
-tone of voice: optimistic, positive, colorful

Side B:
(name of 4 people of the agency:)
Odette, Anne-Sophie, Hortense & Luc-Antoine,
(2 logos)
Pommelin & VelvaRide
(Adres)
Rue des Tilleuls 74 b3 - 1200 Bruxelles - Belgique

Target Market(s)

Movie directors, photographers

Industry/Entity Type

Fashion, advertising & Movies

Requirements
Must have
• SEE TEXT IN BRIEFING

```html
<!DOCTYPE html>
<html lang="en">
<head>
<meta charset="utf-8">
<title>Pommelin &amp; Velvaride — New Year 2026 Card</title>
<link rel="stylesheet" href="https://fonts.googleapis.com/css2?family=Barlow+Condensed:wght@500;600;700&display=swap">
<style>
  :root {
    --page: #e8e8e8;
    --night: #04161d;
    --teal-deep: #0a3a48;
    --teal-glow: #2fc3e0;
    --white: #ffffff;
    --violet: #4a2bd0;
    --sky: #14a6e6;
    --orange: #ec5a14;
    --plum: #5a2a7c;
    --ink-plum: #3d1c5c;
    --ink-orange: #e2541a;
  }
  * { margin: 0; padding: 0; box-sizing: border-box; }
  html, body { width: 1200px; height: 2242px; overflow: hidden; background: var(--page); }
  body { position: relative; font-family: "Barlow Condensed", sans-serif; color: var(--white); }

  .card { position: absolute; left: 80px; width: 1040px; height: 494px; overflow: hidden; }
  .card--front { top: 617px; }
  .card--back { top: 1131px; }

  .studio-scene {
    position: absolute; inset: 0;
    background:
      radial-gradient(ellipse 300px 240px at 930px 230px, rgba(47,195,224,.55), transparent 70%),
      radial-gradient(ellipse 260px 200px at 280px 210px, rgba(30,120,170,.45), transparent 70%),
      radial-gradient(ellipse 600px 180px at 500px 470px, rgba(20,110,130,.55), transparent 75%),
      linear-gradient(180deg, #06222c 0%, var(--night) 55%, var(--teal-deep) 100%);
  }

  .year {
    position: absolute; left: 80px; top: 92px;
    font-weight: 600; font-size: 320px; line-height: 1;
    letter-spacing: -10px; transform: scaleX(.78); transform-origin: left top;
  }
  .motto {
    position: absolute; left: 571px; top: 92px;
    font-weight: 600; font-size: 132px; line-height: 100px; letter-spacing: -1px;
    text-transform: uppercase;
  }
  .motto span { display: block; }

  .team { position: absolute; left: 0; top: 0; width: 579px; }
  .team__band {
    display: flex; align-items: center; gap: 26px;
    padding-left: 40px; border-bottom-right-radius: 14px;
    font-weight: 600; font-size: 76px; text-transform: uppercase; line-height: 1;
    position: relative;
  }
  .team__band--violet { height: 121px; background: linear-gradient(100deg, #5a49d8, var(--violet)); padding-top: 10px; z-index: 4; }
  .team__band--sky { height: 98px; background: var(--sky); margin-top: -12px; padding-top: 12px; z-index: 3; }
  .team__band--orange { height: 89px; background: var(--orange); margin-top: -12px; padding-top: 12px; z-index: 2; }
  .team__band--plum { height: 104px; background: var(--plum); margin-top: -12px; padding-top: 6px; z-index: 1; }
  .tick { width: 48px; height: 36px; flex: none; }

  .brand-panel {
    position: absolute; left: 608px; top: 69px; width: 385px; height: 143px;
    background: var(--white); border-radius: 8px;
    display: flex; align-items: center; justify-content: space-around;
  }
  .brand { font-weight: 600; font-size: 38px; letter-spacing: .5px; }
  .brand--kids { color: var(--ink-plum); }
  .brand--actors { color: var(--ink-orange); }

  .address {
    position: absolute; left: 613px; top: 228px;
    font-weight: 500; font-size: 52px; line-height: 56px;
  }
</style>
</head>
<body>
  <section class="card card--front">
    <div class="studio-scene" role="img" aria-label="Dark teal film studio with a microphone on a stand, a blue spotlight, a hanging bauble and gold snowflake ornaments"></div>
    <div class="year">2026</div>
    <div class="motto"><span>Peace</span><span>and</span><span>Love</span></div>
  </section>

  <section class="card card--back">
    <div class="studio-scene" role="img" aria-label="Empty teal-lit stage with light beams and a spotlight on a tripod"></div>
    <div class="team">
      <div class="team__band team__band--violet">
        <svg class="tick" viewBox="0 0 48 36"><path d="M4 18 L17 30 L44 4" fill="none" stroke="#fff" stroke-width="8" stroke-linejoin="round"/></svg>Odette
      </div>
      <div class="team__band team__band--sky">
        <svg class="tick" viewBox="0 0 48 36"><path d="M4 18 L17 30 L44 4" fill="none" stroke="#fff" stroke-width="8" stroke-linejoin="round"/></svg>Anne-Sophie
      </div>
      <div class="team__band team__band--orange">
        <svg class="tick" viewBox="0 0 48 36"><path d="M4 18 L17 30 L44 4" fill="none" stroke="#fff" stroke-width="8" stroke-linejoin="round"/></svg>Hortense &amp;
      </div>
      <div class="team__band team__band--plum">
        <svg class="tick" viewBox="0 0 48 36"><path d="M4 18 L17 30 L44 4" fill="none" stroke="#fff" stroke-width="8" stroke-linejoin="round"/></svg>Luc-Antoine
      </div>
    </div>
    <div class="brand-panel">
      <span class="brand brand--kids">Pommelin</span>
      <span class="brand brand--actors">VelvaRide</span>
    </div>
    <p class="address">Rue des Tilleuls 74<br>b3 – 1200 Bruxelles –<br>Belgique</p>
  </section>
</body>
</html>
```